Private practice for psychiatry and psychotherapy needs a business card and logo

I need a logo and business card design for my private practice for psychiatry and psychotherapy. The optional names for my practice are: Vornhoute Praktijk voor Psychiatrie en Psychotherapie, or short: Praktijk Vornhoute.
I am a (child and adolescent) psychiatrist and psychotherapist. I diagnose and treat infants, children, adolescents and adults with psychiatric symptoms/disorders. I also give supervision to colleagues about their own treatments. My work is characterised by personal involvement, transparence, creativity and professionality.
I would like to have an appealing, light and bright, yet basic design that invites people (both children and adults) to contact me, gives trust and hope, without loosing professional appearance.
I uploaded my contact information which should not necessarily be all included (in this form) on the card as long as people know how to contact me. Please feel free to be creative!
Please note that my website is only temporarely and need a new design and update too!

Target Market(s)

Clients and patients (children, adolescents, adults) with psychiatric symptoms who need diagnosis and treatment. I work with private clients and patients through medical insurances.

Industry/Entity Type

Mental Health

Contact Information for Business Card

Dr. Sanne Vornhoute-ter Kuilen
Psychiater/Kinder- en Jeugdpsychiater
Wouter Heskampstraat 14
3071 PX Rotterdam
t: 06-51928764
e: info@praktijkvornhoute.nl
i: www.praktijkvornhoute.nl

Logo Text

Praktijk Vornhoute voor Psychiatrie en Psychotherapie; or short: Praktijk Vornhoute

Font styles to use
Sans Serif
Other font styles liked:
• up to designer

Requirements
Must have
• Appealing, light, bright, creative, trustful, professional and unique.

```html
<!DOCTYPE html>
<html lang="nl">
<head>
<meta charset="utf-8">
<title>Praktijk Vornhoute – Visitekaartje</title>
<link rel="stylesheet" href="https://fonts.googleapis.com/css2?family=Open+Sans:wght@400;600&family=Roboto:wght@700&display=swap">
<style>
  :root {
    --backdrop: #e7e9ec;
    --card: #ffffff;
    --accent: #45acdc;
    --ink: #3d3f42;
    --ink-soft: #55585c;
    --shadow: rgba(0, 0, 0, 0.16);
  }
  * { box-sizing: border-box; margin: 0; padding: 0; }
  html, body {
    width: 1200px; height: 1000px; overflow: hidden;
    background: var(--backdrop);
    font-family: "Open Sans", sans-serif;
  }
  .sheet {
    position: relative; width: 1200px; height: 1000px;
  }
  .card {
    position: absolute; left: 250px; width: 700px; height: 400px;
    background: var(--card); border-radius: 18px; overflow: hidden;
    box-shadow: 0 10px 28px var(--shadow);
  }
  .card--front { top: 60px; }
  .card--back { top: 540px; }

  .wordmark {
    display: flex; align-items: center; gap: 12px;
    color: var(--ink-soft); font-weight: 400; letter-spacing: 0.5px;
    text-transform: uppercase; white-space: nowrap;
  }
  .wordmark__dot {
    width: 14px; height: 14px; border-radius: 50%; background: var(--accent);
  }
  .card--front .wordmark {
    position: absolute; left: 50%; top: 50%; transform: translate(-50%, -50%);
    font-size: 28px;
  }

  .holder__tab {
    position: absolute; left: 0; top: 88px; width: 9px; height: 52px;
    background: var(--accent); border-radius: 0 3px 3px 0;
  }
  .holder__name {
    position: absolute; left: 40px; top: 88px;
    font-family: "Roboto", sans-serif; font-weight: 700; font-size: 29px;
    color: var(--ink); text-transform: uppercase; letter-spacing: 0.3px;
  }
  .holder__role {
    position: absolute; left: 40px; top: 124px;
    font-size: 19px; font-weight: 600; color: var(--accent);
  }
  .contact {
    position: absolute; left: 40px; top: 180px; list-style: none;
    font-size: 18px; color: var(--ink-soft); line-height: 1.35;
  }
  .contact__item { display: flex; align-items: flex-start; gap: 14px; }
  .contact__item--address { flex-direction: column; gap: 4px; margin-bottom: 8px; }
  .contact__icon { width: 18px; height: 18px; flex: none; margin-top: 3px; }
  .contact__web-name { color: var(--accent); }

  .card--back .wordmark {
    position: absolute; right: 40px; bottom: 76px; font-size: 22px;
  }
  .band {
    position: absolute; left: 0; right: 0; bottom: 0; height: 40px;
    background: var(--accent);
  }
</style>
</head>
<body>
<main class="sheet">
  <section class="card card--front" aria-label="Voorkant visitekaartje">
    <div class="wordmark"><span class="wordmark__dot"></span>Praktijk Vornhoute</div>
  </section>

  <section class="card card--back" aria-label="Achterkant visitekaartje">
    <span class="holder__tab"></span>
    <h1 class="holder__name">Dr. Sanne Vornhoute-ter Kuilen</h1>
    <p class="holder__role">Psychiater/Kinder- en Jeugdpsychiater</p>

    <ul class="contact">
      <li class="contact__item contact__item--address">
        <svg class="contact__icon" viewBox="0 0 20 20" fill="none" stroke="#45acdc" stroke-width="1.4" stroke-linejoin="round">
          <path d="M2 9 L18 2 L12 18 L9.5 11 Z"/><path d="M9.5 11 L18 2"/>
        </svg>
        <span>Wouter Heskampstraat 14<br>3071 PX Rotterdam</span>
      </li>
      <li class="contact__item">
        <svg class="contact__icon" viewBox="0 0 20 20" fill="#45acdc">
          <path d="M5 2 L8 2 L9 6 L7 8 Q9 12 12 13 L14 11 L18 12 L18 15 Q17 18 14 18 Q4 16 2 6 Q2 3 5 2 Z"/>
        </svg>
        <span>06-51928764</span>
      </li>
      <li class="contact__item">
        <svg class="contact__icon" viewBox="0 0 20 20" fill="#45acdc">
          <path d="M2 5 H18 V15 H2 Z M3 6 L10 11 L17 6" stroke="#fff" stroke-width="1.2"/>
        </svg>
        <span>info@praktijkvornhoute.nl</span>
      </li>
      <li class="contact__item">
        <svg class="contact__icon" viewBox="0 0 20 20" fill="none" stroke="#45acdc" stroke-width="2.2" stroke-linecap="round">
          <circle cx="11" cy="8" r="5.5"/><path d="M7 12 L2.5 17"/>
        </svg>
        <span>www.<span class="contact__web-name">praktijkvornhoute</span>.nl</span>
      </li>
    </ul>

    <div class="wordmark"><span class="wordmark__dot"></span>Praktijk Vornhoute</div>
    <div class="band"></div>
  </section>
</main>
</body>
</html>
```